Book cover design for a collection of poetry - The Lanternfield

Book cover and back design need to be moody, nostalgic, reflective, ethereal. Melancholy and other worldly. Cover design should not be time specific to a period or place but if applicable should reflect British landscape. Book cover should be in tones of blue and must include the title and author (THE LANTERNFIELD BY DORIAN WELKBRIDGE). We love the idea of rain, and looking out of a window. See attached designs. A world you are observing but not in.

Industry/Entity Type

Book Publisher

Font styles to use
Serif
Script

Colors
3176b5
3377b5
85acd3
eaf1f7
0792cd
33a6d7
86cae7
ecf7fb
86cfc6

Requirements
Must have
• The colour blue in it, must be melancholy and reflective.
Nice to have
• Rain in the cover.
Should not have
• Any bright colours.

```html
<!DOCTYPE html>
<html lang="en">
<head>
<meta charset="utf-8">
<title>The Lanternfield – Book Cover</title>
<link rel="stylesheet" href="https://fonts.googleapis.com/css2?family=Arimo:wght@400&family=Tinos:wght@400&display=swap">
<style>
  :root {
    --paper: #ffffff;
    --teal: #037587;
    --teal-deep: #0a3f4a;
    --teal-dark: #062a33;
    --teal-glow: #19a9c9;
    --ink-light: #ffffff;
    --sans: "Arimo", Arial, sans-serif;
    --serif: "Tinos", "Times New Roman", serif;
  }
  * { margin: 0; padding: 0; box-sizing: border-box; }
  html, body { width: 1200px; height: 1000px; overflow: hidden; background: var(--paper); }
  .wrap { position: relative; width: 1200px; height: 1000px; background: var(--paper); }

  /* Back cover */
  .back-cover {
    position: absolute; left: 8px; top: 50px; width: 563px; height: 900px;
    background: var(--teal); color: var(--ink-light); text-align: center;
    font-family: var(--sans);
  }
  .back-cover .headline {
    position: absolute; top: 124px; left: 0; width: 100%;
    font-size: 30px; line-height: 39px; text-transform: uppercase;
  }
  .back-cover .blurb {
    position: absolute; top: 311px; left: 30px; width: 503px;
    font-size: 14.5px; line-height: 20px; text-transform: uppercase;
  }
  .back-cover .blurb p + p { margin-top: 19px; }

  /* Spine */
  .spine {
    position: absolute; left: 571px; top: 50px; width: 57px; height: 900px;
    background: var(--paper); color: var(--teal); font-family: var(--serif);
  }
  .spine .spine-title,
  .spine .spine-author {
    position: absolute; left: 50%; writing-mode: vertical-rl;
    transform: translateX(-50%); white-space: nowrap;
  }
  .spine .spine-title { top: 155px; font-size: 25px; letter-spacing: 4px; }
  .spine .spine-author { top: 538px; font-size: 21px; }

  /* Front cover */
  .front-cover {
    position: absolute; left: 628px; top: 50px; width: 562px; height: 900px;
    overflow: hidden; color: var(--ink-light);
  }
  .front-cover .cover-photo {
    position: absolute; inset: 0;
    background:
      radial-gradient(ellipse 28% 30% at 55% 56%, rgba(120,220,240,0.85) 0%, rgba(40,160,190,0.55) 55%, rgba(0,0,0,0) 100%),
      radial-gradient(ellipse 60% 55% at 55% 50%, #2b9db6 0%, #137a90 45%, var(--teal-deep) 80%, var(--teal-dark) 100%);
  }
  .front-cover .title {
    position: absolute; left: 120px; top: 40px;
    font-family: var(--sans); font-weight: 400; line-height: 1;
  }
  .front-cover .title .the { display: block; font-size: 33px; letter-spacing: 1px; }
  .front-cover .title .main { display: block; margin: 22px 0 0 15px; font-size: 39px; letter-spacing: 4px; }
  .front-cover .author {
    position: absolute; right: 87px; top: 158px;
    font-family: var(--serif); font-size: 25px;
  }
</style>
</head>
<body>
<main class="wrap">
  <section class="back-cover">
    <h2 class="headline">The Lanternfield<br>is a<br>collection of poetry</h2>
    <div class="blurb">
      <p>Told in two parts we first meet Charles –<br>aged, crippled and left alone in his inherited marsh house -<br>reflecting on his life and his marriage to beautiful Alice who we meet in part two. Alice is suicidal, manically depressed and struggling with life as a wife and mother. She meets, harbors and falls in love with a soldier during WWII and her world is changed forever.</p>
      <p>Moving through the 20th century, this life and the next, The Lanternfield interweaves grief, loss, the after-life, mental illness, and ultimately the true nature of love.</p>
    </div>
  </section>

  <section class="spine">
    <span class="spine-title">THE LANTERNFIELD</span>
    <span class="spine-author">Dorian Welkbridge</span>
  </section>

  <section class="front-cover">
    <div class="cover-photo" role="img" aria-label="Rain-streaked four-pane window glowing blue in a dark, weathered stone wall"></div>
    <h1 class="title"><span class="the">THE</span><span class="main">LANTERNFIELD</span></h1>
    <p class="author">Dorian Welkbridge</p>
  </section>
</main>
</body>
</html>
```